Lark Rx discount card
Prescription drug card
We don't need lines for ID numbers.
good job so far. we are looking for rounded corners to make it look like a benefit card not a business card.
I need designs asap. I gave two logos to be used on the Lark Rx Card logo and the Sundial Rx logo which goes on the lower right side smaller than top.
I also gave 5 examples of other cards out there. Look forward to seeing your ideas.

```html
<!DOCTYPE html>
<html lang="en">
<head>
<meta charset="utf-8">
<title>Lark Rx Card – Prescription Savings Card Designs</title>
<link href="https://fonts.googleapis.com/css2?family=Cinzel:wght@700&family=Arimo:wght@400;700&display=swap" rel="stylesheet">
<style>
:root{
  --bg:#e9e4dc;
  --card:#ffffff;
  --red:#c8161d;
  --red-dark:#8e0d12;
  --blue:#1f5fa8;
  --blue-dark:#123c73;
  --navy:#1d2f5e;
  --ink:#222222;
  --stripe:#151515;
  --grey:#d9dde3;
}
*{margin:0;padding:0;box-sizing:border-box}
html,body{width:1200px;height:713px;overflow:hidden}
body{background:var(--bg);font-family:"Arimo",Arial,sans-serif;position:relative}
.card{position:absolute;width:520px;height:300px;border-radius:22px;background:var(--card);overflow:hidden;box-shadow:0 6px 18px rgba(0,0,0,.28)}
.card--classic{left:40px;top:150px}
.card--blue{left:640px;top:180px}
.card--red{left:80px;top:395px}
.band{position:absolute;left:0;right:0}
.header{top:0;height:48px;display:flex;align-items:center;justify-content:center;font-family:"Cinzel",serif;font-weight:700;color:#fff;font-size:24px;letter-spacing:.5px}
.header--red{background:linear-gradient(var(--red),var(--red-dark))}
.header--blue{background:linear-gradient(var(--blue),var(--blue-dark))}
.brand{position:absolute;display:flex;align-items:center;gap:8px}
.brand-dot{width:26px;height:26px;border-radius:50%;background:var(--navy)}
.brand-name{font-family:"Cinzel",serif;font-weight:700;color:var(--navy);font-size:26px;line-height:1}
.tagline{position:absolute;font-size:9px;color:var(--red);font-style:italic}
.benefit{position:absolute;font-weight:700;color:var(--red);font-size:17px}
.small{position:absolute;font-size:9.5px;color:var(--ink);line-height:1.25}
.member{top:140px;height:90px;background:linear-gradient(var(--blue),var(--blue-dark))}
.fields{position:absolute;left:14px;top:10px;width:250px;height:70px;background:#f3f5f8;border-radius:6px;padding:5px 10px;font-size:12px;color:var(--ink);line-height:15px}
.help{position:absolute;right:24px;top:18px;color:#fff;font-weight:700;font-size:17px;text-align:center;line-height:22px}
.stripe{top:112px;height:40px;background:var(--stripe)}
.signline{position:absolute;left:60px;font-size:13px;color:var(--ink);display:flex;align-items:flex-end;gap:14px}
.signline span.line{display:block;width:210px;border-bottom:1px solid #777;height:12px}
.visit{position:absolute;font-size:10px;color:var(--ink)}
.visit a{color:var(--red);text-decoration:none;font-weight:700}
.partner{position:absolute;right:0;background:var(--stripe);color:#fff;font-family:"Cinzel",serif;font-weight:700;font-size:14px;padding:6px 16px 6px 20px;border-radius:14px 0 0 0}
.footer{bottom:0;height:36px;color:#fff;font-size:9px;text-align:center;display:flex;flex-direction:column;justify-content:center;line-height:1.35}
.footer--red{background:linear-gradient(var(--red),var(--red-dark))}
.footer--blue{background:linear-gradient(var(--blue),var(--blue-dark))}
.footer--visit{font-size:11px;text-align:left;padding-left:24px}
</style>
</head>
<body>

<section class="card card--classic">
  <div class="band header header--red">Prescription Savings Card</div>
  <div class="brand" style="left:22px;top:66px"><span class="brand-dot"></span><span class="brand-name">Lark Rx Card</span></div>
  <div class="tagline" style="left:56px;top:98px">Your path to prescription drug savings!</div>
  <div class="benefit" style="left:356px;top:60px;text-align:center;line-height:20px">Enjoy the<br>FREE Benefits!</div>
  <div class="small" style="left:342px;top:104px;width:160px;text-align:center">Save 10% to 70% on Prescription Drugs<br>Accepted at over 50,000 Pharmacies</div>
  <div class="band member">
    <div class="fields">Member Id :<br>Group Id :<br>Bin :<br>Pcn :</div>
    <div class="help">NEED HELP<br>Call: 1-111-111111</div>
  </div>
  <div class="partner" style="bottom:36px">Sundial Rx</div>
  <div class="band footer footer--red footer--visit">for more information please visit: WWW.LARKRXCARD.COM</div>
</section>

<section class="card card--blue">
  <div class="band header header--blue">Prescription Savings Card</div>
  <div class="brand" style="left:22px;top:60px"><span class="brand-dot"></span><span class="brand-name" style="font-size:22px">Lark Rx Card</span></div>
  <div class="tagline" style="left:56px;top:88px">Your path to prescription drug savings!</div>
  <div class="benefit" style="left:300px;top:62px;font-size:15px">Enjoy the FREE Benefits!</div>
  <div class="small" style="left:300px;top:82px">Pharmacist help desk: 1-111-111-111</div>
  <div class="band stripe"></div>
  <div class="signline" style="top:172px">Patient <span class="line"></span></div>
  <div class="signline" style="top:196px">Pharmacist <span class="line" style="width:188px"></span></div>
  <div class="visit" style="left:24px;top:236px">for more information please visit: <a>WWW.LARKRXCARD.COM</a></div>
  <div class="partner" style="bottom:36px">Sundial Rx</div>
  <div class="band footer footer--blue">The FREE card will discount the retail price of your prescription drugs.<br>This is not insurance and this card does not expire.</div>
</section>

<section class="card card--red">
  <div class="band header header--red">Prescription Savings Card</div>
  <div class="brand" style="left:22px;top:60px"><span class="brand-dot"></span><span class="brand-name" style="font-size:22px">Lark Rx Card</span></div>
  <div class="tagline" style="left:56px;top:88px">Your path to prescription drug savings!</div>
  <div class="benefit" style="left:300px;top:62px;font-size:15px">Enjoy the FREE Benefits!</div>
  <div class="small" style="left:300px;top:82px">Pharmacist help desk: 1-111-111-111</div>
  <div class="band stripe"></div>
  <div class="signline" style="top:172px">Patient <span class="line"></span></div>
  <div class="signline" style="top:196px">Pharmacist <span class="line" style="width:188px"></span></div>
  <div class="visit" style="left:24px;top:236px">for more information please visit: <a>WWW.LARKRXCARD.COM</a></div>
  <div class="partner" style="bottom:36px">Sundial Rx</div>
  <div class="band footer footer--red">The FREE card will discount the retail price of your prescription drugs.<br>This is not insurance and this card does not expire.</div>
</section>

</body>
</html>
```